Business Card Design for Consulting Company

I require a Business Card design for my Consulting company. <br/><br/>My company name is: Marek Olvani Consulting Inc.<br/>My website is: www.marekolvaniconsulting.example<br/><br/>My company focuses on management and software development for the Tallobrix CRM platform (www.tallobrix.example)<br/><br/>I have a logo already designed...see attached.
Updates

Also Include my Name and Title: Marek T.L. Olvani President

Target Market(s)

Tallobrix Customers

Contact Information for Business Card

Only include my LOGO (provided)
My Name: Marek TL Olvani
My Title: President
My Company Name: Marek Olvani Consulting Inc.
My Website: www.marekolvaniconsulting.example
My Email: marek.olvani.consulting@mailbox.example

NO PHONE NUMBER
NO ADDRESS

Font styles to use
Serif
Sans Serif
Other font styles liked:
• see my website: www.marekolvaniconsulting.example

Colors

Designer to choose colors to be used in the design.

Requirements
Must have
• Must include my Orange
• Include my name (Marek T.L. Olvani), title (President) company name, website and email
• It should also have a tag line like: Tallobrix Consulting
• I'm flexible with the tag line
Should not have
• Don't include my phone number or address

```html
<!DOCTYPE html>
<html lang="en">
<head>
<meta charset="utf-8">
<title>Marek Olvani Consulting Inc. — Business Card</title>
<link href="https://fonts.googleapis.com/css2?family=Cormorant+SC:wght@500;600&family=Jost:wght@300;400&display=swap" rel="stylesheet">
<style>
  :root {
    --navy: #063d59;
    --navy-swatch: #003e5a;
    --orange: #ec7d23;
    --label: #5a5a5a;
    --page: #ffffff;
  }
  html, body { margin: 0; padding: 0; overflow: hidden; }
  body { background: var(--page); }
  .sheet { position: relative; width: 1200px; height: 891px; overflow: hidden; background: var(--page); }
  .card { position: absolute; background: var(--navy); color: var(--orange); }
  .card--front { left: 172px; top: 125px; width: 329px; height: 576px; }
  .card--back { left: 611px; top: 127px; width: 329px; height: 573px; }
  .serif { font-family: "Cormorant SC", "Times New Roman", serif; font-weight: 600; line-height: 1; position: absolute; margin: 0; white-space: nowrap; }
  .brand-mark { left: 28px; top: 280px; font-size: 22px; letter-spacing: 0.06em; }
  .person-name { left: 28px; top: 363px; font-size: 36px; line-height: 30px; letter-spacing: 0.04em; }
  .front-rule { position: absolute; left: 30px; top: 447px; width: 55px; height: 1.5px; background: var(--orange); }
  .tagline { left: 24px; top: 474px; font-size: 17px; line-height: 15px; letter-spacing: 0.06em; font-weight: 500; }
  .company-name { left: 34px; top: 172px; font-size: 34px; line-height: 26px; letter-spacing: 0.05em; }
  .back-rule { position: absolute; left: 43px; top: 238px; width: 1.5px; height: 183px; background: var(--orange); }
  .contact { position: absolute; left: 32px; top: 435px; margin: 0; font-family: "Jost", Arial, sans-serif; font-weight: 300; font-size: 13.5px; line-height: 23px; white-space: nowrap; }
  .view-label, .palette-title, .swatch-code { position: absolute; font-family: "Jost", Arial, sans-serif; font-weight: 400; color: var(--label); white-space: nowrap; transform: translateX(-50%); margin: 0; }
  .view-label { font-size: 20px; top: 728px; }
  .view-label--front { left: 333px; }
  .view-label--back { left: 761px; }
  .palette-title { left: 1035px; top: 719px; font-size: 19px; letter-spacing: 0.02em; }
  .swatch { position: absolute; width: 58px; height: 58px; border-radius: 50%; top: 753px; }
  .swatch--navy { left: 955px; background: var(--navy-swatch); }
  .swatch--orange { left: 1066px; background: var(--orange); }
  .swatch-code { top: 824px; font-size: 19px; }
  .swatch-code--navy { left: 985px; }
  .swatch-code--orange { left: 1091px; }
</style>
</head>
<body>
<main class="sheet">
  <section class="card card--front" aria-label="Card front">
    <p class="serif brand-mark">Marek Olvani</p>
    <h1 class="serif person-name">Marek<br>T.L. Olvani</h1>
    <div class="front-rule"></div>
    <p class="serif tagline">President Of<br>Tallobrix Consulting</p>
  </section>

  <section class="card card--back" aria-label="Card back">
    <h2 class="serif company-name">Marek Olvani<br>Consulting Inc.</h2>
    <div class="back-rule"></div>
    <p class="contact">www.marekolvaniconsulting.example<br>marek.olvani.consulting@mailbox.example</p>
  </section>

  <p class="view-label view-label--front">FRONT</p>
  <p class="view-label view-label--back">BACK</p>

  <p class="palette-title">COLOR USED:</p>
  <div class="swatch swatch--navy"></div>
  <div class="swatch swatch--orange"></div>
  <p class="swatch-code swatch-code--navy">#003E5A</p>
  <p class="swatch-code swatch-code--orange">#EC7D23</p>
</main>
</body>
</html>
```